website design for Company MVR

Our company name MVR(the grand mural limited), need design a website. It is a website that focuses on promoting art design in the world.
We will provide the existing logo design, the new website and logo should be matched to each other. The website has to include pages "Home" "Contact" "Service" and So on at least 6-8 pages. The site is mainly for publicity and promotion. We will have an existing domain and hosting.
Updates

We prefer the original design, thanks.

Target Market(s)

large public art

Industry/Entity Type

Architecture and design, large public art and sculpture manufacturer

Coding

Coded - Design and coding required

Number of Pages Required

5+ page

Requirements
Must have
• 1. the overall color has to match our logo color 2. Do not need to do any change on our logo including the color 3. Here is a similar style of the home page we like, it can be similar but must not same. Pls check the below link. https://www.velmardo.it/en-us/

```html
<!DOCTYPE html>
<html lang="en">
<head>
<meta charset="utf-8">
<title>MVR – The Grand Mural Limited</title>
<link href="https://fonts.googleapis.com/css2?family=Audiowide&family=Roboto:ital,wght@0,400;0,500;0,700;1,400&display=swap" rel="stylesheet">
<style>
:root{
  --black:#0b0b0b;
  --ink:#1a1a1a;
  --white:#ffffff;
  --grey-text:#6b6b6b;
  --frame:#5a5a5a;
  --footer:#222222;
  --footer-bar:#4a4a4a;
  --star:#f3a712;
  --btn-grey:#4d4d4d;
}
*{box-sizing:border-box;margin:0;padding:0}
html,body{width:1200px;height:4107px;overflow:hidden}
body{position:relative;background:var(--white);font-family:"Roboto",sans-serif;color:var(--ink)}
.abs{position:absolute}
.display{font-family:"Audiowide",sans-serif;text-transform:uppercase;letter-spacing:1px}
.section-title{position:absolute;left:0;width:1200px;text-align:center;font-size:31px;font-family:"Audiowide",sans-serif;text-transform:uppercase;letter-spacing:1px}
.btn{position:absolute;display:flex;align-items:center;justify-content:center;gap:9px;font-size:12px;font-weight:700;text-transform:uppercase;color:var(--white);background:var(--black);border-radius:3px}
.btn svg{width:12px;height:12px}

/* header */
.site-header{left:0;top:0;width:1200px;height:80px;background:var(--white)}
.brand{left:110px;top:22px;font-weight:700;font-size:30px;letter-spacing:1px;color:var(--ink)}
.main-nav{left:413px;top:32px;display:flex;gap:19px;font-size:12px;font-weight:700;text-transform:uppercase}
.main-nav a{color:var(--ink);text-decoration:none}
.main-nav a.active{color:#555;font-weight:500}

/* hero */
.hero{left:0;top:80px;width:1200px;height:560px;background:var(--black);overflow:hidden}
.hero-art{left:560px;top:0;width:640px;height:560px;background:radial-gradient(ellipse at 55% 40%,#3a5a9a 0%,#4a2a6a 25%,#1a1030 55%,var(--black) 80%)}
.hero h1{left:112px;top:158px;font-size:46px;line-height:50px;color:var(--white)}
.hero p{left:112px;top:275px;width:560px;font-size:16px;line-height:26px;color:#eee}
.hero .btn{left:112px;top:346px;width:145px;height:44px;background:var(--btn-grey)}
.dots{left:576px;top:480px;display:flex;gap:16px}

/* about */
.about-frame{left:118px;top:741px;width:457px;height:410px;background:var(--frame);padding:12px}
.about-art{width:100%;height:100%;background:linear-gradient(135deg,#c43b8c 0%,#e8432e 40%,#f06a2b 65%,#f2c530 100%)}
.about h2{left:663px;top:770px;font-size:29px}
.about p{left:663px;top:830px;width:425px;font-size:13.5px;line-height:25.7px;color:var(--grey-text);text-align:justify}
.about .btn{left:663px;top:1089px;width:148px;height:45px}

/* services */
.services{left:0;top:1306px;width:1200px;height:494px;background:linear-gradient(180deg,#2a2a2a,#161616 60%,#222)}
.services .section-title{top:80px;color:var(--white)}
.service-card{top:165px;width:234px;height:206px}
.service-img{width:100%;height:184px;border-radius:4px}
.service-label{position:absolute;left:21px;top:161px;width:191px;height:47px;background:var(--white);border-radius:3px;display:flex;align-items:center;justify-content:center;gap:26px;font-size:13px;font-weight:700;text-transform:uppercase}
.slider-arrow{top:242px;width:34px;height:34px;border-radius:50%;background:var(--white);display:flex;align-items:center;justify-content:center}

/* testimonials */
.testimonials{left:0;top:2601px;width:1200px;height:452px;background:radial-gradient(ellipse at 30% 50%,#f2f2f2,#dcdcdc 70%)}
.testimonials .section-title{top:68px}
.quote-card{top:157px;width:320px;height:143px;background:var(--white);padding:28px 20px;font-style:italic;font-size:13.5px;line-height:28px;color:var(--grey-text);box-shadow:0 2px 8px rgba(0,0,0,.08)}
.quote-card.featured{background:var(--black);color:#ddd}
.quote-card .mark{position:absolute;right:18px;bottom:16px;font-family:"Audiowide",sans-serif;font-size:44px;line-height:30px;font-style:normal;color:var(--black)}
.quote-card.featured .mark{color:#666}
.quote-card.featured::after{content:"";position:absolute;left:20px;bottom:-12px;border:12px solid transparent;border-bottom:0;border-top-color:var(--black)}
.client{top:328px;width:300px;height:52px}
.avatar{position:absolute;left:20px;top:0;width:52px;height:52px;border-radius:50%;background:#b8b8b8;border:3px solid var(--white)}
.client-name{position:absolute;left:87px;top:8px;font-size:14px;font-weight:700;text-transform:uppercase}
.client-role{position:absolute;left:87px;top:28px;font-size:14px;color:var(--grey-text)}
.stars{position:absolute;left:218px;top:14px;color:var(--star);font-size:14px;letter-spacing:1px}

/* blog */
.blog-title{top:3140px;color:var(--ink)}
.blog-card{top:3225px;width:316px;height:375px}
.blog-img{width:316px;height:218px}
.blog-body{position:absolute;left:13px;top:189px;width:290px;height:186px;background:var(--white);box-shadow:0 3px 12px rgba(0,0,0,.12);text-align:center;padding-top:24px}
.blog-meta{font-size:12px;color:var(--grey-text);display:flex;justify-content:center;gap:14px;align-items:center}
.blog-meta i{display:inline-block;width:1px;height:14px;background:#aaa}
.blog-body h3{margin-top:24px;font-size:13px;font-weight:700;text-transform:uppercase}
.blog-body p{margin:20px auto 0;width:250px;font-size:13px;line-height:19px;color:var(--grey-text)}

/* footer */
.site-footer{left:0;top:3706px;width:1200px;height:401px;background:var(--footer);color:var(--white)}
.footer-col{top:77px}
.footer-col h4{font-size:13px;font-weight:700;text-transform:uppercase}
.footer-col h4::after{content:"";display:block;width:50px;height:2px;background:var(--white);margin-top:9px}
.footer-col ul{list-style:none;margin-top:17px}
.footer-col li{font-size:14px;line-height:33px}
.footer-col li::before{content:"»";margin-right:13px}
.footer-brand{left:821px;top:88px;font-weight:700;font-size:80px;letter-spacing:4px;line-height:90px}
.contact-bar{left:163px;top:242px;width:875px;height:58px;background:var(--footer-bar);display:flex;align-items:center}
.contact-item{flex:1;display:flex;align-items:center;justify-content:center;gap:22px;font-size:15px;height:34px}
.contact-item+.contact-item{border-left:1px solid #888}
.contact-icon{width:38px;height:38px;border:1.5px solid var(--white);border-radius:50%;display:flex;align-items:center;justify-content:center}
.copyright{left:0;top:345px;width:1200px;text-align:center;font-size:14px}
</style>
</head>
<body>

<header class="abs site-header">
  <div class="abs brand">MVR</div>
  <nav class="abs main-nav">
    <a class="active" href="#">Home</a><a href="#">About Us</a><a href="#">Our Services</a><a href="#">Latest Blog</a><a href="#">Reviews</a><a href="#">Contact Us</a>
  </nav>
  <div class="btn" style="left:942px;top:17px;width:147px;height:45px">Get Started
    <svg viewBox="0 0 12 12"><circle cx="6" cy="6" r="6" fill="#fff"/><path d="M5 3.5 7.5 6 5 8.5" stroke="#000" stroke-width="1.6" fill="none"/></svg></div>
</header>

<section class="abs hero">
  <div class="abs hero-art" role="img" aria-label="Portrait of a woman surrounded by glowing streaks of coloured light"></div>
  <h1 class="abs display">The Grand Mural<br>Limited</h1>
  <p class="abs">Lorem ipsum dolor sit amet, consectetur adipiscing elit, sed do eiusmod tempor incididunt ut labore et dolore magna aliqua.</p>
  <div class="btn">Get Started
    <svg viewBox="0 0 12 12"><circle cx="6" cy="6" r="6" fill="#fff"/><path d="M5 3.5 7.5 6 5 8.5" stroke="#4d4d4d" stroke-width="1.6" fill="none"/></svg></div>
  <div class="abs dots">
    <svg viewBox="0 0 16 7" width="16" height="7"><circle cx="3.5" cy="3.5" r="3.5" fill="#fff"/><circle cx="12.5" cy="3.5" r="3.5" fill="#fff"/></svg>
    <svg viewBox="0 0 16 7" width="16" height="7"><circle cx="3.5" cy="3.5" r="3.5" fill="#fff"/><circle cx="12.5" cy="3.5" r="3.5" fill="#fff"/></svg>
  </div>
</section>

<section class="about">
  <div class="abs about-frame"><div class="about-art" role="img" aria-label="Vivid oil painting of red, pink and yellow flowers"></div></div>
  <h2 class="abs display">About Us</h2>
  <p class="abs">Sed ut perspiciatis unde omnis iste natus error sit voluptatem accusantium doloremque laudantium, totam rem aperiam, eaque ipsa quae ab illo inventore veritatis et quasi architecto beatae vitae dicta sunt explicabo. Nemo enim ipsam voluptatem quia voluptas sit aspernatur aut odit aut fugit, sed quia consequuntur magni dolores eos qui ratione voluptatem sequi nesciunt. Neque porro quisquam est, qui dolorem ipsum quia dolor sit amet, consectetur, adipisci velit, sed quia non numquam eius modi tempora incidunt ut labore et dolore magnam aliquam</p>
  <div class="btn">Learn More
    <svg viewBox="0 0 12 12"><circle cx="6" cy="6" r="6" fill="#fff"/><path d="M5 3.5 7.5 6 5 8.5" stroke="#000" stroke-width="1.6" fill="none"/></svg></div>
</section>

<section class="abs services">
  <h2 class="section-title">Our Services</h2>
  <div class="abs slider-arrow" style="left:36px"><svg width="12" height="12" viewBox="0 0 12 12"><path d="M8 1 3 6l5 5" stroke="#000" stroke-width="2" fill="none"/></svg></div>
  <div class="abs slider-arrow" style="left:1131px"><svg width="12" height="12" viewBox="0 0 12 12"><path d="M4 1l5 5-5 5" stroke="#000" stroke-width="2" fill="none"/></svg></div>

  <div class="abs service-card" style="left:107px">
    <div class="service-img" role="img" aria-label="Surreal portrait with a bouquet of white flowers" style="background:linear-gradient(160deg,#b9cfc9,#8fa9a3 60%,#c66a44)"></div>
    <div class="service-label">Lorem Ipsum <svg width="13" height="13" viewBox="0 0 12 12"><circle cx="6" cy="6" r="6" fill="#000"/><path d="M5 3.5 7.5 6 5 8.5" stroke="#fff" stroke-width="1.6" fill="none"/></svg></div>
  </div>
  <div class="abs service-card" style="left:357px">
    <div class="service-img" role="img" aria-label="Colourful painted close-up of an eye" style="background:radial-gradient(circle,#1b6d8f,#e0a22a 45%,#c8384a 75%,#6a3a8a)"></div>
    <div class="service-label">Lorem Ipsum <svg width="13" height="13" viewBox="0 0 12 12"><circle cx="6" cy="6" r="6" fill="#000"/><path d="M5 3.5 7.5 6 5 8.5" stroke="#fff" stroke-width="1.6" fill="none"/></svg></div>
  </div>
  <div class="abs service-card" style="left:609px">
    <div class="service-img" role="img" aria-label="Abstract multicoloured swirling paint" style="background:linear-gradient(135deg,#1a1a1a,#d84a2a 35%,#e8c23a 55%,#2a7ac0 80%)"></div>
    <div class="service-label">Lorem Ipsum <svg width="13" height="13" viewBox="0 0 12 12"><circle cx="6" cy="6" r="6" fill="#000"/><path d="M5 3.5 7.5 6 5 8.5" stroke="#fff" stroke-width="1.6" fill="none"/></svg></div>
  </div>
  <div class="abs service-card" style="left:859px">
    <div class="service-img" role="img" aria-label="Pop art painting of a raccoon" style="background:linear-gradient(135deg,#2a3a8a,#d8432a 45%,#2fa3a0 75%,#f0c84a)"></div>
    <div class="service-label">Lorem Ipsum <svg width="13" height="13" viewBox="0 0 12 12"><circle cx="6" cy="6" r="6" fill="#000"/><path d="M5 3.5 7.5 6 5 8.5" stroke="#fff" stroke-width="1.6" fill="none"/></svg></div>
  </div>
</section>

<section class="gallery">
  <h2 class="section-title" style="top:1891px">Our Art Designs</h2>
  <div class="abs" role="img" aria-label="Palette and brushes covered in bright paint" style="left:110px;top:1967px;width:317px;height:225px;background:linear-gradient(135deg,#d8a23a,#2a4ab0 40%,#c83a6a 70%,#3ab0c8)"></div>
  <div class="abs" role="img" aria-label="Watercolour portrait of a woman with red hair" style="left:441px;top:1967px;width:318px;height:225px;background:linear-gradient(135deg,#e8e2de,#d8322a 45%,#f2eeea 80%)"></div>
  <div class="abs" role="img" aria-label="Flowing rainbow brush strokes" style="left:772px;top:1967px;width:318px;height:225px;background:linear-gradient(160deg,#2a2a6a,#d83a5a 35%,#e8a23a 55%,#3a8ac8 85%)"></div>
  <div class="abs" role="img" aria-label="Abstract red dots over teal and orange paint" style="left:110px;top:2208px;width:483px;height:285px;background:linear-gradient(135deg,#c83a2a,#2a6a7a 45%,#e0782a 75%,#8a2a1a)"></div>
  <div class="abs" role="img" aria-label="Watercolour face in blue, green and yellow" style="left:607px;top:2208px;width:483px;height:285px;background:linear-gradient(135deg,#d8e8e0,#7ac0d8 45%,#3a8a5a 70%,#e8d24a)"></div>
</section>

<section class="abs testimonials">
  <h2 class="section-title">What Our Clients Say</h2>
  <div class="abs quote-card" style="left:110px">Lorem ipsum dolor sit amet, consectetur adipiscing elit, sed do eiusmod tempor incididunt ut labore et dolore<span class="mark">”</span></div>
  <div class="abs quote-card featured" style="left:440px">Lorem ipsum dolor sit amet, consectetur adipiscing elit, sed do eiusmod tempor incididunt ut labore et dolore<span class="mark">”</span></div>
  <div class="abs quote-card" style="left:768px">Lorem ipsum dolor sit amet, consectetur adipiscing elit, sed do eiusmod tempor incididunt ut labore et dolore<span class="mark">”</span></div>

  <div class="abs client" style="left:110px"><div class="avatar" role="img" aria-label="Client photo"></div><div class="client-name">Lucas</div><div class="client-role">Businessman</div><div class="stars">★★★★★</div></div>
  <div class="abs client" style="left:440px"><div class="avatar" role="img" aria-label="Client photo"></div><div class="client-name">Daniel</div><div class="client-role">Businessman</div><div class="stars">★★★★★</div></div>
  <div class="abs client" style="left:768px"><div class="avatar" role="img" aria-label="Client photo"></div><div class="client-name">Clara Benson</div><div class="client-role">Businessman</div><div class="stars">★★★★★</div></div>
</section>

<section class="blog">
  <h2 class="section-title blog-title">Latest Blog</h2>
  <article class="abs blog-card" style="left:104px">
    <div class="blog-img" role="img" aria-label="Neon paint splashed sculpture artwork" style="background:linear-gradient(135deg,#e83aa0,#3ab04a 40%,#f0d23a 65%,#2a3ab0)"></div>
    <div class="blog-body"><div class="blog-meta"><span>▦ Jul 20 , 2021</span><i></i><span>● John Doe</span></div><h3>Lorem Ipsum Dolor Sit</h3><p>Sed ut perspiciatis unde omnis ist natus error sit voluptatem accusantium doloremque laudantium, totam</p></div>
  </article>
  <article class="abs blog-card" style="left:442px">
    <div class="blog-img" role="img" aria-label="Brush mixing red and yellow paint" style="background:linear-gradient(160deg,#5a3a2a,#e8a23a 40%,#d8322a 70%,#3a2a2a)"></div>
    <div class="blog-body"><div class="blog-meta"><span>▦ Jul 20 , 2021</span><i></i><span>● John Doe</span></div><h3>Lorem Ipsum Dolor Sit</h3><p>Sed ut perspiciatis unde omnis ist natus error sit voluptatem accusantium doloremque laudantium, totam</p></div>
  </article>
  <article class="abs blog-card" style="left:779px">
    <div class="blog-img" role="img" aria-label="Body painting in bright stripes of colour" style="background:linear-gradient(135deg,#1a2a7a,#c83a2a 40%,#e8b23a 65%,#2a8a4a)"></div>
    <div class="blog-body"><div class="blog-meta"><span>▦ Jul 20 , 2021</span><i></i><span>● John Doe</span></div><h3>Lorem Ipsum Dolor Sit</h3><p>Sed ut perspiciatis unde omnis ist natus error sit voluptatem accusantium doloremque laudantium, totam</p></div>
  </article>
</section>

<footer class="abs site-footer">
  <div class="abs footer-col" style="left:115px"><h4>Quick Links</h4><ul><li>Home</li><li>About Us</li><li>Our Services</li></ul></div>
  <div class="abs footer-col" style="left:355px"><h4>Other Links</h4><ul><li>Terms Of Use</li><li>Privacy Policy</li><li>Contact Us</li></ul></div>
  <div class="abs footer-col" style="left:618px"><h4>Useful Links</h4><ul><li>FAQ</li><li>Team Members</li><li>Help Service</li></ul></div>
  <div class="abs footer-brand">MVR</div>
  <div class="abs contact-bar">
    <div class="contact-item"><span class="contact-icon"><svg width="18" height="18" viewBox="0 0 24 24"><path d="M6.6 10.8a15 15 0 0 0 6.6 6.6l2.2-2.2c.3-.3.7-.4 1-.2 1.1.4 2.3.6 3.6.6.6 0 1 .4 1 1V20c0 .6-.4 1-1 1A17 17 0 0 1 3 4c0-.6.4-1 1-1h3.5c.6 0 1 .4 1 1 0 1.3.2 2.5.6 3.6.1.3 0 .7-.2 1z" fill="none" stroke="#fff" stroke-width="1.6"/></svg></span>1 800 555 014</div>
    <div class="contact-item"><span class="contact-icon"><svg width="18" height="18" viewBox="0 0 24 24"><rect x="5" y="8" width="14" height="12" rx="2" fill="none" stroke="#fff" stroke-width="1.6"/><path d="M8 8V4h8v4M9 12h2M13 12h2M9 15h2M13 15h2" stroke="#fff" stroke-width="1.6"/></svg></span>1 800 555 099</div>
    <div class="contact-item"><span class="contact-icon"><svg width="18" height="18" viewBox="0 0 24 24"><rect x="3" y="5" width="18" height="14" rx="2" fill="none" stroke="#fff" stroke-width="1.6"/><path d="m3 7 9 6 9-6" fill="none" stroke="#fff" stroke-width="1.6"/></svg></span>info@mvr.com.au</div>
  </div>
  <div class="abs copyright">© 2021 The grand mural limited. All Rights Reserved</div>
</footer>

</body>
</html>
```